International Food Manufacturer in the need of a new business card and logo.

Our Company - Northgate Pantry Ltd.

Our Industry - Food and Drink

We are a Wild Harvested Food Distributor / Manufacturer. We service the following food sectors: Supermarkets, Hotels, Restaurants, Cafes, Catering and all people looking to eat healthy food products.

Slogan - The foremost source for everything healthy

Business card details -

48-52 Marlow Lane
Hatherby Green
London
EC9Z 4RT United Kingdom
Dennis Prowle
+44 7000 481736 - UK
+971 50 7739205 - UAE
+38 063 914 2758 - Ukraine
dennis@northgatepantry.example
www.northgatepantry.example

Goal - We are looking for a dynamic modern new look for our corporate image and a designer who can bring this new concept to our future food product designs. Please try to incorporate 3d hexagonal vector Imaging in your design concepts.

Target Market(s)

Industry/Entity Type

Food Service

Contact Information for Business Card

Northgate Pantry Ltd.
48-52 Marlow Lane
Hatherby Green
London
EC9Z 4RT United Kingdom
Dennis Prowle
+44 7000 481736 - UK
+971 50 7739205 - UAE

Font styles to use
Serif

Colors

Designer to choose colors to be used in the design.

Requirements
Must have
• Please read project description above.
Nice to have
Should not have

```html
<!DOCTYPE html>
<html lang="en">
<head>
<meta charset="utf-8">
<title>Northgate Pantry Ltd. – Business Card</title>
<link rel="stylesheet" href="https://fonts.googleapis.com/css2?family=Cinzel:wght@500;600&family=Lato:wght@400&display=swap">
<style>
  :root {
    --page-bg: #ecebe8;
    --leaf-green: #56ab08;
    --tomato-red: #ea0e0f;
    --card-white: #ffffff;
    --disc-edge: #dcdcdc;
    --ink-dark: #1e1e1e;
  }
  * { box-sizing: border-box; margin: 0; padding: 0; }
  html, body {
    width: 1200px; height: 900px; overflow: hidden;
    background: var(--page-bg);
  }
  .business-card {
    position: absolute; left: 160px; top: 178px;
    width: 880px; height: 544px;
    background: var(--tomato-red);
    box-shadow: 0 14px 40px rgba(0,0,0,0.18);
    overflow: hidden;
  }
  .green-panel {
    position: absolute; left: 0; top: 0;
    width: 624px; height: 100%;
    background: var(--leaf-green);
  }
  .card-holder-name {
    position: absolute; left: 39px; top: 58px;
    font-family: "Cinzel", serif; font-weight: 600;
    font-size: 34px; letter-spacing: 0.5px;
    color: var(--card-white);
  }
  .contact-block {
    position: absolute; left: 39px;
    font-family: "Lato", sans-serif; font-size: 24px;
    line-height: 32px; color: var(--card-white);
    list-style: none;
  }
  .address { top: 163px; }
  .phones { top: 322px; }
  .online { top: 431px; }
  .contact-block li { display: flex; align-items: center; gap: 6px; white-space: nowrap; }
  .contact-icon { width: 18px; height: 18px; flex: none; fill: var(--card-white); }
  .brand-disc {
    position: absolute; left: 419px; top: 58px;
    width: 430px; height: 430px; border-radius: 50%;
    background: radial-gradient(circle at 45% 40%, #ffffff 0%, #f4f4f4 60%, var(--disc-edge) 100%);
    display: flex; flex-direction: column; align-items: center; justify-content: center;
    text-align: center;
  }
  .brand-mark {
    width: 26px; height: 26px; border-radius: 50%;
    background: var(--leaf-green); margin-bottom: 16px;
  }
  .brand-name {
    font-family: "Cinzel", serif; font-weight: 500;
    font-size: 27px; color: var(--leaf-green); letter-spacing: 0.5px;
  }
  .brand-slogan {
    margin-top: 26px;
    font-family: "Lato", sans-serif; font-size: 18px; line-height: 24px;
    color: var(--ink-dark); letter-spacing: 0.3px;
  }
</style>
</head>
<body>
  <article class="business-card">
    <div class="green-panel"></div>

    <h1 class="card-holder-name">DENNIS PROWLE</h1>

    <ul class="contact-block address">
      <li>Northgate Pantry Ltd.</li>
      <li>48-52 Marlow Lane</li>
      <li>Hatherby Green London</li>
      <li>EC9Z 4RT United Kingdom</li>
    </ul>

    <ul class="contact-block phones">
      <li><svg class="contact-icon" viewBox="0 0 20 20"><path d="M2 7c0-2 3-4 8-4s8 2 8 4v1.5h-4V7c-1-.6-2.4-.9-4-.9S7 6.4 6 7v1.5H2z"/><path d="M4 10h12l1 6H3z"/></svg>+44 7000 481736 (UK)</li>
      <li><svg class="contact-icon" viewBox="0 0 20 20"><path d="M2 7c0-2 3-4 8-4s8 2 8 4v1.5h-4V7c-1-.6-2.4-.9-4-.9S7 6.4 6 7v1.5H2z"/><path d="M4 10h12l1 6H3z"/></svg>+971 50 7739205 (UAE)</li>
      <li><svg class="contact-icon" viewBox="0 0 20 20"><path d="M2 7c0-2 3-4 8-4s8 2 8 4v1.5h-4V7c-1-.6-2.4-.9-4-.9S7 6.4 6 7v1.5H2z"/><path d="M4 10h12l1 6H3z"/></svg>+38 063 914 2758 (Ukraine)</li>
    </ul>

    <ul class="contact-block online">
      <li><svg class="contact-icon" viewBox="0 0 20 20"><path d="M2 4h16v12H2z M3.5 5.5v.4L10 11l6.5-5.1v-.4z" fill-rule="evenodd"/></svg>dennis@northgatepantry.example</li>
      <li><svg class="contact-icon" viewBox="0 0 20 20"><circle cx="10" cy="10" r="8"/><path d="M6 6c2 0 3 1 2.5 2.5S6 10 7 12s0 3-1 3M13 4.5c-1 1.5 0 2.5 1.5 3s1 2.5 0 3.5" stroke="#56ab08" stroke-width="1.6" fill="none"/></svg>www.northgatepantry.example</li>
    </ul>

    <div class="brand-disc">
      <span class="brand-mark"></span>
      <p class="brand-name">NORTHGATE PANTRY LTD.</p>
      <p class="brand-slogan">THE FINEST PANTRY OF<br>WILD HARVESTED FOOD</p>
    </div>
  </article>
</body>
</html>
```